Advertisement Design Project

Money Nest is a financial services provider operating a network of 50+ payday loan and check cashing centers across Ontario.

We are launching a special promotion for our Payday Loan product.

Specifically, the promotion is a "New Customer Acquisition Strategy” whereby we are incentifying new customers who have not had a payday loan with us.

Design: “Penny Week - $100 Loan for $ 1 - First Loan”

The promotion is a $100 payday loan for $1.

We want to create a unique trademark/emblem/icon to advertise our ‘Penny Week’ promotion.

The design will be placed in the form of a window decal on our store front windows and on flyers, etc.

With respect to choice of color, we are looking for something that will grab motorists and walk by traffic when they look at our store front.

Our company colors are red/black on Yellow, however, this Point of Purchase decal does not necessarily have to be the branded the same unless you feel this color is more impactful than others.

We certainly want the “$100 loan for $1” to the center point of the design.

Since this is a decal the design does not necessarily have to be a box or rectangle…certain words/phrases, etc. can protrude outside of the design.

In general we have two decal sizes, 2 feet in diameter and 3 feet in diameter (depending on the store front windows of some of our branches).

Also, the emblem/icon/logo needs to have some fine print [somewhere towards the bottom]

*Offer applies to first time Payday Loan customers only, or customers that have not initiated a Payday Loan in the last 12 months prior to the present date. Not valid with any other offers
and valid at participating Money Nest locations only. Limit one offer per customer. Limited time offer. The cost of borrowing at Money Nest is $21 per each $100 advanced. On a $300 loan for 14 days, the cost of borrowing is $63, with a total payback amount of $363. The maximum allowable cost of borrowing under payday loan agreements is $21 per each $100 advanced.

Thanks,
Tomas

Industry/Entity Type

Financial

```html
<!DOCTYPE html>
<html lang="en">
<head>
<meta charset="utf-8">
<title>Money Nest — Penny Week Window Decal</title>
<link rel="stylesheet" href="https://fonts.googleapis.com/css2?family=Anton&family=Nunito:wght@800;900&family=Lato:ital,wght@0,900;1,900&display=swap">
<style>
  :root {
    --paper: #ffffff;
    --decal-yellow: #fff024;
    --decal-glow: #fffbe0;
    --brand-red: #e8202a;
    --ink: #111111;
    --panel-shadow: #9a9a9a;
  }
  html, body {
    margin: 0;
    padding: 0;
    width: 1200px;
    height: 1200px;
    overflow: hidden;
    background: var(--paper);
  }
  .decal {
    display: block;
    width: 1200px;
    height: 1200px;
  }
  .decal__shadow { fill: var(--panel-shadow); }
  .decal__panel { fill: url(#panelGlow); }

  .brand-name {
    font-family: "Anton", "Arial Narrow", sans-serif;
    font-size: 84px;
    fill: var(--brand-red);
  }
  .presents {
    font-family: "Lato", Arial, sans-serif;
    font-style: italic;
    font-weight: 900;
    font-size: 31px;
    fill: var(--ink);
  }
  .promo-name,
  .headline {
    font-family: "Anton", "Arial Narrow", sans-serif;
    fill: var(--brand-red);
  }
  .promo-name {
    font-size: 70px;
    filter: drop-shadow(4px 4px 0 var(--ink));
  }
  .headline {
    font-size: 138px;
    filter: drop-shadow(6px 6px 0 var(--ink));
  }

  .bag-art { fill: var(--brand-red); }

  .cta-band__shadow { fill: var(--ink); }
  .cta-band__fill { fill: var(--brand-red); }
  .cta-band__text {
    font-family: "Nunito", Arial, sans-serif;
    font-weight: 900;
    font-size: 50px;
    fill: var(--decal-yellow);
    filter: drop-shadow(3px 3px 0 var(--ink));
  }
  .cta-band__brand {
    filter: none;
  }

  .fine-print {
    font-family: "Lato", Arial, sans-serif;
    font-weight: 900;
    font-size: 11px;
    fill: var(--ink);
  }
</style>
</head>
<body>
<svg class="decal" viewBox="0 0 1200 1200" xmlns="http://www.w3.org/2000/svg" aria-label="Money Nest Penny Week window decal">
  <defs>
    <radialGradient id="panelGlow" cx="560" cy="620" r="520" gradientUnits="userSpaceOnUse">
      <stop offset="0" stop-color="var(--decal-glow)" style="stop-color: var(--decal-glow)"/>
      <stop offset="0.45" stop-color="var(--decal-yellow)" style="stop-color: var(--decal-yellow)"/>
      <stop offset="1" stop-color="var(--decal-yellow)" style="stop-color: var(--decal-yellow)"/>
    </radialGradient>
  </defs>

  <!-- Arched decal panel -->
  <path class="decal__shadow" d="M70,263 H206 A660,660 0 0 1 1006,263 H1153 V1146 H70 Z"/>
  <path class="decal__panel" d="M64,257 H200 A660,660 0 0 1 1000,257 H1147 V1140 H64 Z"/>

  <!-- Brand and promotion title -->
  <text class="brand-name" x="590" y="228" text-anchor="middle">MONEY NEST</text>
  <text class="presents" x="590" y="311" text-anchor="middle">presents</text>
  <text class="promo-name" x="590" y="410" text-anchor="middle" textLength="460" lengthAdjust="spacingAndGlyphs">“PENNY WEEK”</text>
  <text class="headline" x="600" y="555" text-anchor="middle" textLength="1000" lengthAdjust="spacingAndGlyphs">$100 Loan for $ 1</text>

  <!-- Money bag illustration area -->
  <rect class="bag-art" x="130" y="605" width="405" height="515" rx="180" role="img" aria-label="Illustration: red money bag with a large black dollar sign"/>

  <!-- Call to action band -->
  <polygon class="cta-band__shadow" points="527,637 1153,637 1153,880 600,880"/>
  <polygon class="cta-band__fill" points="557,650 1147,650 1147,873 624,873"/>
  <text class="cta-band__text" x="853" y="704" text-anchor="middle">Visit your nearest</text>
  <text class="cta-band__text" x="853" y="780" text-anchor="middle"><tspan class="cta-band__brand">Money Nest</tspan> store to</text>
  <text class="cta-band__text" x="853" y="855" text-anchor="middle">avail the scheme.</text>

  <!-- Fine print -->
  <text class="fine-print" x="580">
    <tspan x="580" y="937">*Offer applies to first time Payday Loan customers only, or customers that have not initi-</tspan>
    <tspan x="580" y="963">ated a Payday Loan in the last 12 months prior to the present date. Not valid with any</tspan>
    <tspan x="580" y="986">other offers</tspan>
    <tspan x="580" y="1010">and valid at participating Money Nest locations only. Limit one offer per customer. Limited</tspan>
    <tspan x="580" y="1036">time offer. The cost of borrowing at Money Nest is $21 per each $100 advanced. On a $300</tspan>
    <tspan x="580" y="1062">loan for 14 days, the cost of borrowing is $63, with a total payback amount of $363. The</tspan>
    <tspan x="580" y="1088">maximum allowable cost of borrowing under payday loan agreements is $21 per each</tspan>
    <tspan x="580" y="1115">$100 advanced.</tspan>
  </text>
</svg>
</body>
</html>
```